Need webdesign for service company that provides Car hiring service and transit service

We need a web design for a company that provides airport transit services and transport services including Limo, Corporate cars, Disability transit, Family transit service. We need is a simple and professional design.

Below is site which we like and also offer the same service http://www.ridelyntrek.com.au/

Reason: Waiting for the Feedback from multiple stakeholders. Need the time to select and approve the design

Target Market(s)

Tourism, Travel

Industry/Entity Type

Airport

Number of Pages Required

3 page

Font styles to use
Decorative
Script

Requirements
Must have
• Simple and Professional, Site we like http://www.ridelyntrek.com.au/ and also need to mobile friendly
Should not have
• Shouldn't have too many images

```html
<!DOCTYPE html>
<html lang="en">
<head>
<meta charset="utf-8">
<title>Roveway – Private &amp; Business Transport</title>
<link href="https://fonts.googleapis.com/css2?family=Open+Sans:wght@400;600;700&family=Nunito+Sans:wght@400;600;700&display=swap" rel="stylesheet">
<style>
:root{
  --white:#ffffff;
  --ink:#111111;
  --muted:#444444;
  --hero-a:#e9eaeb;
  --hero-b:#d6d8da;
  --hero-c:#c9c6c2;
  --panel:rgba(105,100,100,0.88);
  --tile-dark:rgba(45,45,45,0.92);
  --tile-mid:rgba(110,108,108,0.9);
  --tile-soft:rgba(128,124,124,0.82);
  --tile-light:rgba(150,145,145,0.85);
  --yellow:#ffcc00;
  --button-ink:#555555;
}
*{box-sizing:border-box;margin:0;padding:0}
html,body{width:1200px;height:1123px;overflow:hidden;background:var(--white)}
body{position:relative;font-family:'Nunito Sans',sans-serif;color:var(--ink)}
a{text-decoration:none}
.site-header{position:absolute;left:0;top:0;width:1200px;height:98px;background:var(--white)}
.brand{position:absolute;left:140px;top:30px;display:flex;align-items:center;gap:12px}
.brand-mark{width:36px;height:36px;border:3px solid var(--ink)}
.brand-name{font-family:'Open Sans',sans-serif;font-weight:600;font-size:30px;letter-spacing:0.5px;color:var(--ink);line-height:1}
.header-actions{position:absolute;left:890px;top:21px;display:flex;gap:9px}
.header-actions svg{width:54px;height:54px}
.hero{position:absolute;left:0;top:98px;width:1200px;height:932px;overflow:hidden}
.hero-photo{position:absolute;inset:0;background:linear-gradient(90deg,var(--hero-a) 0%,var(--hero-c) 45%,var(--hero-b) 60%,var(--hero-a) 100%)}
.hero-title{position:absolute;left:0;width:1200px;top:42px;text-align:center;font-family:'Open Sans',sans-serif;font-size:34px;font-weight:400;line-height:1.2}
.hero-subtitle{position:absolute;left:0;width:1200px;top:84px;text-align:center;font-size:17px;line-height:1.2}
.hero-text{position:absolute;left:0;width:1200px;top:127px;text-align:center;font-size:15px;line-height:21px}
.quote-panel{position:absolute;left:142px;top:231px;width:385px;height:377px;background:var(--panel);color:var(--white)}
.quote-title{position:absolute;left:31px;top:28px;font-family:'Open Sans',sans-serif;font-size:22px;font-weight:400;line-height:1.2}
.quote-field{position:absolute;left:32px;width:308px;height:45px;background:var(--white);display:flex;align-items:center;font-family:'Open Sans',sans-serif;font-size:11.5px;color:#333}
.quote-field .field-icon{width:40px;height:29px;border-right:1px solid #ccc;display:flex;align-items:center;justify-content:center;margin-right:14px;flex:none}
.field-origin{top:81px}
.field-destination{top:137px}
.quote-option{position:absolute;left:38px;display:flex;align-items:center;gap:10px;font-family:'Open Sans',sans-serif;font-size:11px;font-weight:600;letter-spacing:0.2px;line-height:14px}
.option-stops{top:201px}
.option-vehicles{top:232px}
.estimate-button{position:absolute;left:32px;top:279px;width:308px;height:58px;background:var(--yellow);color:var(--button-ink);font-family:'Open Sans',sans-serif;font-weight:700;font-size:24px;display:flex;align-items:center;justify-content:center;letter-spacing:0.3px}
.service-tile{position:absolute;color:var(--white);font-family:'Open Sans',sans-serif;font-size:16px;text-align:center;display:flex;flex-direction:column;align-items:center}
.service-tile svg{display:block}
.tile-limo{left:560px;top:229px;width:154px;height:123px;background:var(--tile-dark);padding-top:36px;gap:20px}
.tile-corporate{left:720px;top:231px;width:166px;height:123px;background:var(--tile-mid);padding-top:28px;gap:16px}
.tile-disability{left:893px;top:231px;width:166px;height:123px;background:var(--tile-mid);padding-top:26px;gap:12px}
.tile-transport{left:560px;top:359px;width:154px;height:249px;background:var(--tile-soft);padding-top:68px;gap:18px;line-height:22px}
.tile-airport{left:720px;top:359px;width:339px;height:123px;background:var(--tile-light);padding-top:26px;gap:14px;font-weight:600}
.tile-driver{left:720px;top:487px;width:166px;height:123px;background:var(--tile-light);padding-top:20px;gap:12px;font-weight:600}
.tile-contact{left:893px;top:487px;width:166px;height:123px;background:var(--tile-dark);padding-top:28px;gap:18px;font-weight:600}
.news-title{position:absolute;left:0;width:1200px;top:680px;text-align:center;font-family:'Open Sans',sans-serif;font-size:34px;font-weight:400;line-height:1.2}
.news-text{position:absolute;left:0;width:1200px;top:750px;text-align:center;font-size:17px;line-height:28px}
.news-arrow{position:absolute;top:755px}
.arrow-prev{left:326px}
.arrow-next{left:838px}
.read-more{position:absolute;left:544px;top:844px;width:112px;height:36px;background:var(--ink);color:var(--white);font-size:13px;font-weight:700;display:flex;align-items:center;justify-content:center}
.site-footer{position:absolute;left:0;top:1030px;width:1200px;height:93px;background:var(--white)}
.footer-mark{position:absolute;left:136px;top:38px;width:20px;height:20px;border:2px solid var(--ink)}
.copyright{position:absolute;left:174px;top:40px;font-size:10.5px}
.footer-links{position:absolute;right:129px;top:40px;font-size:10.5px;word-spacing:1px}
</style>
</head>
<body>
<header class="site-header">
  <div class="brand"><span class="brand-mark"></span><span class="brand-name">ROVEWAY</span></div>
  <nav class="header-actions">
    <svg viewBox="0 0 54 54"><rect x="11" y="11" width="32" height="32" transform="rotate(45 27 27)" fill="none" stroke="#111" stroke-width="1.6"/><path d="M20 22h14M20 27h14M20 32h14" stroke="#111" stroke-width="2.6"/></svg>
    <svg viewBox="0 0 54 54"><rect x="11" y="11" width="32" height="32" transform="rotate(45 27 27)" fill="none" stroke="#111" stroke-width="1.6"/><path d="M21 20c1-1 3-1 3 0l2 4-2 2c1 2 3 4 5 5l2-2 4 2c1 0 1 2 0 3-2 2-5 2-9-2s-6-9-5-12z" fill="#111"/></svg>
    <svg viewBox="0 0 54 54"><rect x="11" y="11" width="32" height="32" transform="rotate(45 27 27)" fill="none" stroke="#111" stroke-width="1.6"/><circle cx="25" cy="25" r="5" fill="none" stroke="#111" stroke-width="2.4"/><path d="M29 29l5 5" stroke="#111" stroke-width="2.6"/></svg>
  </nav>
</header>

<main class="hero">
  <div class="hero-photo" role="img" aria-label="Soft light photo of a business traveller on the phone walking with a suitcase along a city street"></div>
  <h1 class="hero-title">Private &amp; Business</h1>
  <p class="hero-subtitle">Personalised Transport Service</p>
  <p class="hero-text">It is a long established fact that a reader will be distracted by the<br>readable content of a page when looking.</p>

  <section class="quote-panel">
    <h2 class="quote-title">Get Instant Quote</h2>
    <div class="quote-field field-origin"><span class="field-icon"><svg width="11" height="11"><circle cx="5.5" cy="5.5" r="4.3" fill="none" stroke="#555" stroke-width="1.4"/></svg></span>Origin (Public Location or Exact Address</div>
    <div class="quote-field field-destination"><span class="field-icon"><svg width="10" height="13"><path d="M5 12C2 8 1 6 1 4.5a4 4 0 018 0C9 6 8 8 5 12z" fill="#555"/><circle cx="5" cy="4.5" r="1.5" fill="#fff"/></svg></span>Destination (Public Location or Exact Address</div>
    <div class="quote-option option-stops"><svg width="12" height="12"><path d="M6 0v12M0 6h12" stroke="#fff" stroke-width="2.6"/></svg>ADD STOPS</div>
    <div class="quote-option option-vehicles"><svg width="13" height="11"><path d="M1 5l2-4h7l2 4v5h-2V9H3v1H1z" fill="#fff"/><circle cx="3.5" cy="6.5" r="1" fill="#6a6565"/><circle cx="9.5" cy="6.5" r="1" fill="#6a6565"/></svg>SHOW OTHER VEHICLES</div>
    <div class="estimate-button">ESTIMATE FARE</div>
  </section>

  <a class="service-tile tile-limo"><svg width="90" height="20" viewBox="0 0 90 20"><path d="M2 13c0-3 4-4 10-5l10-5h44l8 5c6 0 12 1 14 4v3H2z" fill="#fff"/><circle cx="14" cy="15" r="4" fill="#fff" stroke="#333" stroke-width="2"/><circle cx="76" cy="15" r="4" fill="#fff" stroke="#333" stroke-width="2"/></svg>Limo</a>
  <a class="service-tile tile-corporate"><svg width="70" height="30" viewBox="0 0 70 30"><path d="M3 20v-7l7-2 6-9h30l10 9c8 1 11 3 11 6v3z" fill="#fff"/><path d="M19 4h11v7H15zM33 4h11l7 7H33z" fill="#777"/><circle cx="15" cy="22" r="5" fill="#ddd" stroke="#777" stroke-width="2"/><circle cx="55" cy="22" r="5" fill="#ddd" stroke="#777" stroke-width="2"/></svg>Corporate cars</a>
  <a class="service-tile tile-disability"><svg width="46" height="40" viewBox="0 0 46 40"><rect x="6" y="7" width="34" height="20" fill="none" stroke="#fff" stroke-width="2.6"/><path d="M16 7V2h14v5" fill="none" stroke="#fff" stroke-width="2.6"/><g fill="#fff"><circle cx="3" cy="36" r="2"/><circle cx="11" cy="36" r="2"/><circle cx="19" cy="36" r="2"/><circle cx="27" cy="36" r="2"/><circle cx="35" cy="36" r="2"/><circle cx="43" cy="36" r="2"/></g></svg>Disability transit</a>
  <a class="service-tile tile-transport"><svg width="84" height="32" viewBox="0 0 84 32"><path d="M8 2h52v22H8zM60 8h12l6 8v8H60z" fill="none" stroke="#fff" stroke-width="3"/><rect x="14" y="8" width="40" height="8" fill="none" stroke="#fff" stroke-width="1.5"/><circle cx="18" cy="25" r="3.5" fill="#fff"/><circle cx="68" cy="25" r="3.5" fill="#fff"/><path d="M0 30h84" stroke="#fff" stroke-width="2.5"/></svg>Transport<br>Services</a>
  <a class="service-tile tile-airport"><svg width="70" height="46" viewBox="0 0 70 46"><path d="M10 2l4 0 4 14 14 4 6-8 4 1-2 10 20 6c3 1 3 4 0 4L10 20z" fill="#fff"/><path d="M4 42h62" stroke="#fff" stroke-width="3"/></svg>Airport Transit</a>
  <a class="service-tile tile-driver"><svg width="58" height="56" viewBox="0 0 58 56"><path d="M13 10c0-6 32-6 32 0l-3 6H16z" fill="#fff"/><circle cx="29" cy="26" r="9" fill="#fff"/><path d="M6 54c0-12 8-18 16-18l7 10 7-10c8 0 16 6 16 18z" fill="#fff"/></svg>Become a Driver</a>
  <a class="service-tile tile-contact"><svg width="52" height="38" viewBox="0 0 52 38"><rect x="2" y="2" width="48" height="34" fill="none" stroke="#fff" stroke-width="3"/><path d="M2 3l24 19 24-19" fill="none" stroke="#fff" stroke-width="3"/></svg>Contact</a>

  <h2 class="news-title">News &amp; Events</h2>
  <p class="news-text">Lorem Ipsum is simply dummy text of the printing and<br>typese industry Lorem Ipsum has been</p>
  <svg class="news-arrow arrow-prev" width="24" height="32" viewBox="0 0 24 32"><path d="M18 3L6 16l12 13" fill="none" stroke="#888" stroke-width="4"/></svg>
  <svg class="news-arrow arrow-next" width="24" height="32" viewBox="0 0 24 32"><path d="M6 3l12 13L6 29" fill="none" stroke="#888" stroke-width="4"/></svg>
  <a class="read-more">READ MORE</a>
</main>

<footer class="site-footer">
  <span class="footer-mark"></span>
  <p class="copyright">Copyrihgts @ 2017 All Rights Reserved</p>
  <p class="footer-links">Home &nbsp;| &nbsp;Sitemap | &nbsp;Privacy policy &nbsp;| &nbsp;Terms &amp; Conditions</p>
</footer>
</body>
</html>
```